Professional Website for Brightfold Laundry Company

Brightfold Laundry Company is a family-owned laundry service provider that has been serving Midtown Atlanta for over 45 years. We provide express clothing and linen washing services to residential and commercial clients in Atlanta and surrounding areas.

The final website and logo design should convey professionalism and give the customer a sense of security in having their personal items laundered with us.

Target Market(s)

Commercial Businesses and high net worth personal customers

Industry/Entity Type

Professional Laundry Services

Coding

Coded - Design and coding required

Number of Pages Required

5+ page

Font styles to use
Sans Serif

Colors
0054AA
0677BA
7BADD7
CADEEF
E8F1F8

Requirements
Must have
• I would like to have the following elements on my website: 1. Blog page 2. Contact Us Form 3. Sign up for service (sample attached) 4. Sections outlined in the content copy page 5. Links to social media accounts.
Nice to have
• A great example is https://www.quillmarsh.example/laundry-pick-up-and-delivery/?utm_term=pick%20up%20and%20delivery%20laundry%20service&utm_campaign=*QM%20United%20States%20%7C%20Search%20(Broad%20KWs)&utm_source=zorvik&utm_medium=ppc&hsa_acc=1111111111&hsa_cam=22222222222&hsa_grp=3333333333333333&hsa_ad=&hsa_src=o&hsa_tgt=kwd-44444444444444:loc-100&hsa_kw=pick%20up%20and%20delivery%20laundry%20service&hsa_mt=e&hsa_net=zorvik&hsa_ver=3&msclkid=00000000000000000000000000000000

```html
<!DOCTYPE html>
<html lang="en">
<head>
<meta charset="utf-8">
<title>Brightfold Laundry Company</title>
<link href="https://fonts.googleapis.com/css2?family=Jost:wght@300;400;500;600;700&family=Montserrat:wght@800&display=swap" rel="stylesheet">
<style>
:root{
  --navy:#0054AA;
  --blue:#0677BA;
  --mid:#7BADD7;
  --pale:#CADEEF;
  --mist:#E8F1F8;
  --ink:#1d1d1f;
  --text:#3a3a3a;
  --white:#ffffff;
}
*{box-sizing:border-box;margin:0;padding:0}
html,body{width:1200px;height:3998px;overflow:hidden;background:var(--white)}
body{font-family:'Jost',sans-serif;color:var(--text)}
.page{position:relative;width:1200px;height:3998px;overflow:hidden}
.abs{position:absolute}

/* header */
.topbar{position:absolute;left:560px;top:0;width:640px;height:47px;background:var(--navy);border-bottom-left-radius:40px;display:flex;align-items:center;justify-content:flex-end;gap:42px;padding-right:110px;color:var(--white);font-size:16px}
.topbar span{display:flex;align-items:center;gap:12px}
.logo-tab{position:absolute;left:100px;top:0;width:248px;height:135px;background:var(--white);border-radius:0 0 60px 60px;z-index:3;display:flex;align-items:center;justify-content:center;text-align:center}
.brand{font-family:'Jost',sans-serif;font-weight:500;color:#2b2b2b;letter-spacing:2px;line-height:1.15;font-size:26px;text-transform:uppercase}
.brand small{display:block;font-size:17px;letter-spacing:3px}
.nav{position:absolute;top:70px;right:110px;display:flex;gap:46px;font-size:18px;color:#222;z-index:3}
.nav .active{font-weight:600}

/* hero */
.hero{position:absolute;left:0;top:115px;width:1200px;height:650px;background:linear-gradient(180deg,#e3eef8 0%,#b6d0ea 35%,#6f9fd3 75%,#4f86c6 100%)}
.hero-wave{position:absolute;left:0;top:560px}
.hero-welcome{position:absolute;left:112px;top:300px;font-size:38px;font-weight:400;color:var(--white);display:flex;align-items:center;gap:20px}
.hero-welcome i{display:block;width:72px;height:2px;background:var(--white)}
.hero-title{position:absolute;left:112px;top:350px;font-family:'Montserrat',sans-serif;font-weight:800;font-size:54px;line-height:64px;color:var(--white);text-shadow:0 3px 8px rgba(0,40,100,.25)}
.btn-outline-light{position:absolute;left:112px;top:506px;width:144px;height:50px;border:3px solid var(--white);border-radius:25px;color:var(--white);font-size:19px;display:flex;align-items:center;justify-content:center}
.ph{background:linear-gradient(160deg,#f4f6f8,#d9dee4)}

/* headings */
.sec-title{position:absolute;left:0;width:1200px;text-align:center;font-weight:700;color:var(--navy);font-size:44px;letter-spacing:.5px}
.rule{position:absolute;display:flex;gap:18px}
.rule i{display:block;width:60px;height:3px;background:#333}

/* steps */
.step-circle{position:absolute;width:140px;height:140px;border-radius:50%;background:linear-gradient(140deg,#9ab7d8,#6c92bf);display:flex;align-items:center;justify-content:center}
.step-num{position:absolute;font-size:50px;font-weight:700;color:rgba(123,173,215,.18)}
.step-title{position:absolute;width:300px;text-align:center;font-size:19px;font-weight:500;color:#111;line-height:29px}
.step-text{position:absolute;width:300px;text-align:center;font-size:14px;line-height:28px;color:#333}

/* about */
.about-bg{position:absolute;left:0;top:1340px;width:1200px;height:600px;background:linear-gradient(180deg,var(--mist),#dbe9f5 50%,var(--mist))}
.about-title{position:absolute;left:562px;top:1425px;font-size:44px;font-weight:700;color:var(--navy)}
.about-rule{position:absolute;left:562px;top:1485px;width:60px;height:3px;background:#333}
.about-rule.b{left:640px}
.about-text{position:absolute;left:562px;top:1515px;width:526px;font-size:17px;line-height:30.4px;text-align:justify;color:#333}
.about-text p+p{margin-top:5px}
.btn-outline{position:absolute;width:144px;height:50px;border:2px solid var(--navy);border-radius:25px;color:var(--navy);font-size:19px;display:flex;align-items:center;justify-content:center}

/* services */
.card{position:absolute;top:2131px;width:290px;height:376px;background:var(--white);border-radius:16px;box-shadow:0 4px 14px rgba(0,40,90,.16);overflow:hidden;text-align:center}
.card-media{height:198px;border-bottom:4px solid #4d6f95}
.card h3{margin-top:16px;font-size:17px;font-weight:500;color:#111}
.card p{margin:6px 18px 0;font-size:14px;line-height:28px;color:#444}
.card a{display:inline-block;margin-top:8px;font-size:14px;color:var(--blue);font-weight:500;text-decoration:none}
.arrow-btn{position:absolute;top:2304px;width:32px;height:32px}

/* faq */
.faq-bg{position:absolute;left:0;top:2620px;width:1200px;height:1000px;background:linear-gradient(180deg,#dbe9f5,var(--mist) 40%,#d6e6f3)}
.faq{position:absolute;left:110px;width:978px;background:var(--white);box-shadow:0 2px 6px rgba(0,40,90,.1)}
.faq-q{height:82px;display:flex;align-items:center;justify-content:space-between;padding:0 13px 0 32px;font-size:17px;font-weight:500;color:#111}
.faq-toggle{width:66px;height:50px;background:var(--blue);display:flex;align-items:center;justify-content:center}
.faq.open .faq-q{background:#e8ebee}
.faq.open .faq-toggle{background:var(--white)}
.faq-a{padding:24px 32px 30px;font-size:17px;line-height:30.4px;color:#333}
.faq-a b{color:var(--blue);font-weight:500}

/* footer */
.fnav{position:absolute;top:3727px;right:110px;display:flex;gap:46px;font-size:18px;color:#222}
.fline{position:absolute;left:110px;top:3790px;width:978px;height:1px;background:#ddd}
.fcol{position:absolute;top:3828px;font-size:16px;line-height:28px;color:#333}
.fcol h4{font-size:16px;font-weight:600;color:#111;display:flex;align-items:center;gap:10px;margin-bottom:12px;text-transform:uppercase}
.fdiv{position:absolute;top:3822px;width:1px;height:94px;background:#ddd}
.social{display:flex;gap:12px;margin-top:4px}
.social i{display:block;width:46px;height:46px;border-radius:50%;background:var(--navy)}
.copy{position:absolute;top:3962px;left:0;width:1200px;text-align:center;font-size:16px;color:#333}
</style>
</head>
<body>
<div class="page">

  <!-- header -->
  <div class="topbar">
    <span><svg width="16" height="16" viewBox="0 0 24 24"><path fill="#fff" d="M6.6 10.8a15.1 15.1 0 0 0 6.6 6.6l2.2-2.2a1 1 0 0 1 1-.25 11.4 11.4 0 0 0 3.6.57 1 1 0 0 1 1 1V20a1 1 0 0 1-1 1A17 17 0 0 1 3 4a1 1 0 0 1 1-1h3.5a1 1 0 0 1 1 1c0 1.25.2 2.45.57 3.57a1 1 0 0 1-.25 1z"/></svg>Call:+1800-555-0142</span>
    <span><svg width="18" height="14" viewBox="0 0 24 18"><path fill="#fff" d="M2 0h20a2 2 0 0 1 2 2v14a2 2 0 0 1-2 2H2a2 2 0 0 1-2-2V2a2 2 0 0 1 2-2zm10 8L2 2v2l10 6 10-6V2z"/></svg>Mail:info@brightfoldlaundry.example</span>
  </div>
  <div class="logo-tab"><div class="brand">Brightfold<br>Laundry<small>Company</small></div></div>
  <nav class="nav"><span class="active">Home</span><span>Our Services</span><span>About Us</span><span>Price</span><span>Contact Us</span></nav>

  <!-- hero -->
  <section class="hero">
    <svg class="hero-wave" width="1200" height="100" viewBox="0 0 1200 100" preserveAspectRatio="none"><path fill="#fff" d="M0 100 L0 70 C120 110 300 100 480 60 C640 25 820 10 980 40 C1080 60 1150 40 1200 10 L1200 100 Z"/></svg>
  </section>
  <div class="abs ph" role="img" aria-label="Front-loading white washing machine" style="left:757px;top:244px;width:330px;height:470px;border-radius:8px"></div>
  <div class="abs" role="img" aria-label="Woven laundry basket with folded towels" style="left:554px;top:535px;width:246px;height:188px;border-radius:20px 20px 60px 60px;background:linear-gradient(180deg,#dfe6ee,#c9936c)"></div>
  <div class="hero-welcome">WELCOME TO <i></i></div>
  <h1 class="hero-title">BRIGHTFOLD LAUNDRY<br>COMPANY</h1>
  <div class="btn-outline-light">Get Started</div>

  <!-- setting up services -->
  <h2 class="sec-title" style="top:812px">SETTING UP SERVICES</h2>
  <div class="rule" style="left:531px;top:876px"><i></i><i></i></div>

  <svg class="abs" style="left:0;top:990px" width="1200" height="100" viewBox="0 0 1200 100"><path d="M306 30 C360 20 390 80 430 85 C480 90 480 30 522 20 M660 20 C700 20 730 60 780 55 C830 50 850 30 887 18" fill="none" stroke="#b9bcc0" stroke-width="2.5" stroke-dasharray="7 6"/></svg>

  <div class="step-num" style="left:260px;top:1038px">01</div>
  <div class="step-num" style="left:617px;top:1038px">02</div>
  <div class="step-num" style="left:983px;top:1038px">03</div>

  <div class="step-circle" style="left:166px;top:932px"><svg width="64" height="64" viewBox="0 0 64 64" fill="none" stroke="#fff" stroke-width="3"><circle cx="28" cy="18" r="11"/><path d="M8 54c0-12 9-20 20-20 4 0 7 1 10 2"/><circle cx="46" cy="46" r="10"/><path d="M46 40v12M40 46h12"/></svg></div>
  <div class="step-circle" style="left:521px;top:932px"><svg width="64" height="64" viewBox="0 0 64 64" fill="none" stroke="#fff" stroke-width="3"><path d="M40 56H12V8h28v14"/><path d="M18 18h16M18 26h16M18 34h10M18 42h8"/><path d="M52 22l6 6-20 20-8 2 2-8z"/></svg></div>
  <div class="step-circle" style="left:886px;top:932px"><svg width="64" height="64" viewBox="0 0 64 64" fill="none" stroke="#fff" stroke-width="3"><path d="M24 6h22l8 6v26H24z"/><path d="M30 6c0 6 10 6 10 0"/><path d="M6 40h12l10 4h14a4 4 0 0 1 0 8H28M6 58l16-2 30-10a4 4 0 0 0-3-7"/></svg></div>

  <div class="step-title" style="left:86px;top:1100px">SIGN UP</div>
  <div class="step-text" style="left:86px;top:1140px">Give us a call at 404-555-0187 or use our sign up page to schedule service. You can control the frequency of how often we process your laundry.</div>
  <div class="step-title" style="left:441px;top:1100px">FILL OUT A CUSTOMER<br>PROFILE</div>
  <div class="step-text" style="left:441px;top:1166px;width:290px;margin-left:5px">When setting up your customer profile you can detail how you want your laundry processed</div>
  <div class="step-title" style="left:806px;top:1100px">SCHEDULE A PICKUP</div>
  <div class="step-text" style="left:806px;top:1140px">Place your clothes in the Brightfold Laundry Company bag and leave it out on your scheduled pickup day.</div>

  <!-- about -->
  <div class="about-bg"></div>
  <svg class="abs" style="left:0;top:1330px" width="1200" height="40" viewBox="0 0 1200 40" preserveAspectRatio="none"><path fill="#fff" d="M0 0H1200V14C1000 2 800 30 600 22 380 14 200 4 0 20Z"/></svg>
  <svg class="abs" style="left:0;top:1912px" width="1200" height="32" viewBox="0 0 1200 32" preserveAspectRatio="none"><path fill="#fff" d="M0 32H1200V14C1000 30 800 4 600 12 380 20 200 30 0 12Z"/></svg>
  <div class="abs" style="left:136px;top:1446px;width:368px;height:384px;border-radius:50%;background:var(--mid)"></div>
  <div class="abs" role="img" aria-label="Smiling woman carrying a laundry basket beside washing machines" style="left:112px;top:1444px;width:380px;height:380px;border-radius:50%;background:linear-gradient(150deg,#c8d2dc,#8da0b4 60%,#4d6a8a)"></div>
  <h2 class="about-title">ABOUT US</h2>
  <div class="about-rule"></div><div class="about-rule b"></div>
  <div class="about-text">
    <p>Brightfold Laundry Company is a family-owned laundry service provider that has been serving Midtown Atlanta for over 45 years. We are proud to offer high quality and convenient services to the area residents and business owners and strive to keep our customers' clothing in tip top shape.</p>
    <p>Whether you have commercial laundry needs, are washing clothes for your family, or want to relax that weekend and have us pick up and wash/dry/fold for you, the professionals at Brightfold Laundry Company are ready to meet your goals.</p>
  </div>
  <div class="btn-outline" style="left:562px;top:1824px">Get Started</div>

  <!-- services -->
  <h2 class="sec-title" style="top:2004px">OUR SERVICES</h2>
  <div class="rule" style="left:531px;top:2068px"><i></i><i></i></div>

  <svg class="arrow-btn" style="left:35px" viewBox="0 0 32 32"><circle cx="16" cy="16" r="14.5" fill="none" stroke="#666" stroke-width="1.6"/><path d="M22 16H10M15 11l-5 5 5 5" fill="none" stroke="#666" stroke-width="1.6"/></svg>
  <svg class="arrow-btn" style="left:1127px" viewBox="0 0 32 32"><circle cx="16" cy="16" r="14.5" fill="none" stroke="var(--blue)" stroke-width="1.6"/><path d="M10 16h12M17 11l5 5-5 5" fill="none" stroke="var(--blue)" stroke-width="1.6"/></svg>

  <article class="card" style="left:110px">
    <div class="card-media" role="img" aria-label="Woman loading a commercial washing machine" style="background:linear-gradient(150deg,#b9c1c9,#6f7a86)"></div>
    <h3>Light Commercial Services</h3>
    <p>Daycare Centers, Dog Groomers, Massage Therapists, Hair Salons, Fitness Clubs, Dentists...</p>
    <a>Learn More &#8594;</a>
  </article>
  <article class="card" style="left:453px">
    <div class="card-media" role="img" aria-label="Professional ironing a shirt in a dry cleaning shop" style="background:linear-gradient(150deg,#c7d4e2,#5d86b4)"></div>
    <h3>Professional Laundry Services</h3>
    <p>If you want to enjoy the perks of dry cleaning without all the chemicals, we offer a wash, dry...</p>
    <a>Learn More &#8594;</a>
  </article>
  <article class="card" style="left:798px">
    <div class="card-media" role="img" aria-label="Courier holding a laundry box beside a delivery van" style="background:linear-gradient(150deg,#e4e6e9,#9ea7b1)"></div>
    <h3>Pickup and Delivery</h3>
    <p>Pickup and delivery available in the Atlanta, Midtown and Buckhead area.</p>
    <a>Learn More &#8594;</a>
  </article>

  <!-- what to expect -->
  <div class="faq-bg"></div>
  <svg class="abs" style="left:0;top:2610px" width="1200" height="40" viewBox="0 0 1200 40" preserveAspectRatio="none"><path fill="#fff" d="M0 0H1200V10C1000 30 800 2 600 14 380 26 200 6 0 22Z"/></svg>
  <h2 class="sec-title" style="top:2712px">WHAT TO EXPECT</h2>
  <div class="rule" style="left:531px;top:2776px"><i></i><i></i></div>

  <div class="faq" style="top:2834px"><div class="faq-q">Can I Customize My Service?<span class="faq-toggle"><svg width="22" height="22"><path d="M11 1v20M1 11h20" stroke="#fff" stroke-width="2"/></svg></span></div></div>
  <div class="faq open" style="top:2930px">
    <div class="faq-q">Are Laundry Bags Provided?<span class="faq-toggle"><svg width="22" height="22"><path d="M1 11h20" stroke="#333" stroke-width="2"/></svg></span></div>
    <div class="faq-a">We will provide you an Brightfold Laundry Company laundry bag marked with your name. All you need to do is simply leave your laundry out on the day of pickup. If this is your initial pick up, we recommend a disposable bag marked with your name and <b>“Brightfold Laundry Company”</b>.incididunt?</div>
  </div>
  <div class="faq" style="top:3174px"><div class="faq-q">What is the Turnaround Time?<span class="faq-toggle"><svg width="22" height="22"><path d="M11 1v20M1 11h20" stroke="#fff" stroke-width="2"/></svg></span></div></div>
  <div class="faq" style="top:3269px"><div class="faq-q">How Do We Pay?<span class="faq-toggle"><svg width="22" height="22"><path d="M11 1v20M1 11h20" stroke="#fff" stroke-width="2"/></svg></span></div></div>
  <div class="faq" style="top:3363px"><div class="faq-q">Do you have a referral program?<span class="faq-toggle"><svg width="22" height="22"><path d="M11 1v20M1 11h20" stroke="#fff" stroke-width="2"/></svg></span></div></div>
  <div class="faq" style="top:3458px"><div class="faq-q">Are you open on the Holidays?<span class="faq-toggle"><svg width="22" height="22"><path d="M11 1v20M1 11h20" stroke="#fff" stroke-width="2"/></svg></span></div></div>
  <svg class="abs" style="left:0;top:3590px" width="1200" height="32" viewBox="0 0 1200 32" preserveAspectRatio="none"><path fill="#fff" d="M0 32H1200V8C1000 28 800 6 600 16 380 26 200 30 0 10Z"/></svg>

  <!-- footer -->
  <div class="abs brand" style="left:108px;top:3660px;text-align:center;width:190px">Brightfold<br>Laundry<small>Company</small></div>
  <nav class="fnav"><span>Home</span><span>Our Services</span><span>About Us</span><span>Price</span><span>Contact Us</span></nav>
  <div class="fline"></div>

  <div class="fcol" style="left:114px"><h4><svg width="10" height="14" viewBox="0 0 10 14"><path fill="var(--navy)" d="M5 0a5 5 0 0 1 5 5c0 4-5 9-5 9S0 9 0 5a5 5 0 0 1 5-5zm0 3a2 2 0 1 0 0 4 2 2 0 0 0 0-4z"/></svg>Address</h4>Brightfold Laundry Company,<br>Address comes here</div>
  <div class="fdiv" style="left:348px"></div>
  <div class="fcol" style="left:400px"><h4><svg width="13" height="13" viewBox="0 0 24 24"><path fill="var(--navy)" d="M6.6 10.8a15.1 15.1 0 0 0 6.6 6.6l2.2-2.2a1 1 0 0 1 1-.25 11.4 11.4 0 0 0 3.6.57 1 1 0 0 1 1 1V20a1 1 0 0 1-1 1A17 17 0 0 1 3 4a1 1 0 0 1 1-1h3.5a1 1 0 0 1 1 1c0 1.25.2 2.45.57 3.57a1 1 0 0 1-.25 1z"/></svg>Phone</h4>+1800-555-0142</div>
  <div class="fdiv" style="left:576px"></div>
  <div class="fcol" style="left:633px"><h4><svg width="15" height="11" viewBox="0 0 24 18"><path fill="var(--navy)" d="M2 0h20a2 2 0 0 1 2 2v14a2 2 0 0 1-2 2H2a2 2 0 0 1-2-2V2a2 2 0 0 1 2-2zm10 8L2 2v2l10 6 10-6V2z"/></svg>E-mail</h4>info@brightfoldlaundry.example</div>
  <div class="fdiv" style="left:857px"></div>
  <div class="fcol" style="left:915px"><h4>Sociale Media</h4><div class="social"><i></i><i></i></div></div>

  <div class="copy">2022 Brightfold Laundry Company. All Rights Reserved.</div>
</div>
</body>
</html>
```